Velmora Outcomes Brochure Design Project

- Who we are?
Velmora Outcomes is New Internet Marketing Company Based in China.

It is our aim to provide Chinese clients with the means to internationally market their product, via the Internet.

Our primary products are Outsourced Design ( Thanks to Pixel hive and the amazing designers who use it), SEO and Virtual Hosting.

- Project Brief
Design a vibrant and fresh brochure that introduces the fundamentals of SEO. There is no restriction to the number of pages, however all the info I have included in this brief must be included.

- Colour Palette
Please see link or download the Adobe Swatch Exchange File or follow the link below
http://tintaro.example.com/#themes/search?term=5830716
Updates

Logo updated - grey background removed

Various file formats added for logo and brochure content

Brochure zip file add containing logo in different formats.

Adobe color scheme file added

The general corporate colors are:

Base Color: CMYK :0, 60, 80, 0  Hex: FF6633
Dark Orange: CMYK: 0, 72, 96, 30 Hex: B23308
Light Orange: CMYK 0, 42, 56, 0 Hex: FF9571
Grey: CMYK 0, 0, 0, 48 Hex: 858585
Light Grey: CMYK 0, 0, 0, 26 Hex: BDBDBD

Please note that I'm happy for other colors to be included, however I would like these the corporate branding colors to be clearly present through the brochure.

Hi All

First place payment has increased to $600 - Looking to see some creative designs!

Hi All

Project Deadline Extended
Reason: I have increase the budget and extend the deadline as I need to see more design.

I have attached a zip file that contains example brochures I like.

We are not keen on the table data its a little plain. We have create an info-graphic to replace one of the table and would like to see it included in the design.

Project Deadline Extended
Reason: A few designers have asked for this extension and I would like to see additional designs. Thanks Marek

Target Market(s)

- Our Target Audience is..
It is small to medium businesses looking to reach out to the international market.
Our clients still very much operate on a face to face level in business and are new to the concept of Internet marketing

However this must look professional, Marketable and Clean, with the power of connecting people globally, through SEO and design to be reflected visually in the brochure.

Industry/Entity Type

Internet

Requirements
Must have
• One or more of the FACTS that I have highlighted need to stand out on each page. These FACTS can be found the document attached to this brief and are under the section titled 'Did You Know!'. Not every fact in this section needs to be highlighted in the brochure, but each page needs to have at least, one or more fact that stands out, soemwhere on the page.
See attached document, under the heading 'Did you Know!' and use one or two of these facts to spruce up the pages!

One image/ per page or per two pages MUST be included!

- Provide stock photos and please send us a message with the additional cost of these with your submission

The Table data, that I have included in the attachment must be included in the body of the pages - BUT the table format is not necessary and you can place the information in the body like plain text.

The brochure size should be a little larger than A4.

Please design the back page, like a pocket to hold paper and other material in it that I include with this brochure.

```html
<!DOCTYPE html>
<html lang="en">
<head>
<meta charset="utf-8">
<title>Our Method vs the Traditional Method</title>
<link href="https://fonts.googleapis.com/css2?family=Marcellus+SC&family=Arimo:wght@400;700&display=swap" rel="stylesheet">
<style>
  :root {
    --orange: #ff6633;
    --dark-orange: #b23308;
    --light-orange: #ff9571;
    --grey: #858585;
    --light-grey: #bdbdbd;
    --row-tint: #fbe2d9;
    --label-tint: #f8d6ca;
    --head-tint: #f4b9a4;
    --ink: #2b2b2b;
    --page: #ffffff;
  }
  * { box-sizing: border-box; margin: 0; padding: 0; }
  html, body { width: 863px; height: 1200px; overflow: hidden; background: var(--page); }
  .page { position: relative; width: 863px; height: 1200px; background: var(--page); font-family: "Arimo", Arial, sans-serif; color: var(--ink); }
  .hero-photo {
    position: absolute; left: 0; top: 0; width: 863px; height: 310px;
    background: linear-gradient(180deg, #8d8f92 0%, #c9cacc 45%, #e9e9ea 70%, #f5f5f5 100%);
  }
  .hero-swoosh { position: absolute; left: 0; top: 230px; width: 863px; height: 140px; }
  .section-title {
    position: absolute; left: 43px; top: 352px;
    font-family: "Marcellus SC", "Times New Roman", serif;
    font-size: 27px; letter-spacing: 2px; color: var(--orange);
  }
  .comparison {
    position: absolute; left: 43px; top: 395px; width: 782px;
    border-collapse: collapse; font-size: 14.5px; line-height: 1.3; text-align: center;
  }
  .comparison th, .comparison td { border: 1px solid #e8c3b6; padding: 6px 10px; vertical-align: middle; }
  .comparison thead th { height: 30px; font-weight: 400; background: var(--page); }
  .comparison thead th.traditional { background: var(--head-tint); }
  .comparison th.row-label { background: var(--label-tint); font-weight: 400; width: 202px; }
  .comparison tbody tr:nth-child(odd) td { background: var(--row-tint); }
  .comparison tbody tr:nth-child(even) td { background: var(--page); }
  .col-our-short { width: 115px; }
  .col-our-long { width: 145px; }
  .col-trad-short { width: 145px; }
  .footnote {
    position: absolute; left: 43px; top: 1112px; width: 790px;
    font-size: 14.5px; line-height: 1.45; color: var(--grey);
  }
</style>
</head>
<body>
<main class="page">
  <div class="hero-photo" role="img" aria-label="Photo of a businesswoman working at a laptop beside office stairs, with a person carrying a briefcase walking up the steps"></div>
  <svg class="hero-swoosh" viewBox="0 0 863 140" aria-hidden="true">
    <path d="M0 95 C 250 55, 560 20, 863 0 L 863 140 L 0 140 Z" fill="var(--page)"/>
    <path d="M0 70 C 260 45, 560 25, 863 10 L 863 45 C 580 55, 300 85, 0 115 Z" fill="var(--orange)"/>
    <path d="M0 62 C 270 38, 570 18, 863 4 L 863 12 C 570 27, 270 48, 0 72 Z" fill="var(--dark-orange)"/>
    <path d="M0 115 C 300 85, 580 55, 863 45 L 863 58 C 580 66, 300 95, 0 126 Z" fill="var(--light-orange)"/>
  </svg>

  <h1 class="section-title">Our Method vs the Traditional Method</h1>

  <table class="comparison">
    <thead>
      <tr>
        <th></th>
        <th colspan="2">Our Method</th>
        <th colspan="2" class="traditional">Traditional</th>
      </tr>
    </thead>
    <tbody>
      <tr style="height:190px">
        <th class="row-label">Cost</th>
        <td class="col-our-short">Low Cost</td>
        <td class="col-our-long">You only pay for the winning designs - you don't pay for anything else</td>
        <td class="col-trad-short">High Cost</td>
        <td>Traditional design companies have to cover the cost of the designers on every project, you ultimately pay for these cost</td>
      </tr>
      <tr style="height:35px">
        <th class="row-label">Number of Design</th>
        <td>A Lot</td>
        <td>100~20</td>
        <td>A few</td>
        <td>3-7</td>
      </tr>
      <tr style="height:165px">
        <th class="row-label">Variety of Designs</th>
        <td>Many unique International Designs</td>
        <td>Many of your designs will come from different people from all over the globe this ensures that every design is unique</td>
        <td>A Few similar designs</td>
        <td>Many design companies have all its designers in a single location and only assign 1 or 2 designers to your project, so that design progress becomes stale</td>
      </tr>
      <tr style="height:60px">
        <th class="row-label">Numbers of Designers</th>
        <td>Many International Designer</td>
        <td>15-60+</td>
        <td>A Small department team</td>
        <td>2-3</td>
      </tr>
      <tr style="height:35px">
        <th class="row-label">Number of changes</th>
        <td colspan="2">Too many count</td>
        <td colspan="2">On a single 2-3</td>
      </tr>
      <tr style="height:165px">
        <th class="row-label">Number of Designers to choice from</th>
        <td>10000~</td>
        <td>We have thousands of freelance designers that we invite to your project</td>
        <td>5-1000</td>
        <td>Even the biggest design companies can only spare a few employes to work on a project</td>
      </tr>
    </tbody>
  </table>

  <p class="footnote">Normally a design project takes between 10 and 15 days... but don't worry if you are in a rush - we have created projects with amazing results in less than 5 days.</p>
</main>
</body>
</html>
```